Australian Solar Smart Home Provider needs business card design

We need a simple, clean, business card that shows who we are and gives the brand feeling. Please see the website (www.plovenix.com) and the attached logo as well. Please use this logo on the business card. As a business we do residential solar, batteries, smart home technology, and hot water solutions. We want the feeling to be accessible to ages 40-65 but at the same time be a bit on the technologically savvy side.
Also the primary purpose of the business card is to hand of and drive referrals - so we want everyone to have a referral code on the card and that aspect should stand out.
Things we want on the card with an example employee:
Name: Marcus Pellwood
Position: Director of Sales and Marketing
telephone number office: 02 8765 4312
telephone number mobile: 0428 915 603
address: Suite 402, 18 Brindle Lane, Sydney, NSW 2000
website: www.plovenix.com
Target Market(s)
Homeowners aged 35-60
Industry/Entity Type
Residential
Contact Information for Business Card
Name: Marcus Pellwood
website: www.plovenix.com
referral code: Mpellwood
Look and feel

```html
<!DOCTYPE html>
<html lang="en">
<head>
<meta charset="utf-8">
<title>Plovenix Business Card</title>
<link rel="stylesheet" href="https://fonts.googleapis.com/css2?family=Ubuntu:wght@400;500;700&family=Mulish:wght@700;800&display=swap">
<style>
  :root {
    --bg: #e4e4e4;
    --card: #ffffff;
    --green: #a8c814;
    --green-dark: #7b9a1c;
    --grey-text: #4a4a55;
    --logo-grey: #8a8a8a;
    --logo-circle: #d6d6d6;
    --white: #ffffff;
  }
  * { box-sizing: border-box; margin: 0; padding: 0; }
  html, body { width: 1200px; height: 1000px; overflow: hidden; }
  body { background: var(--bg); position: relative; font-family: "Ubuntu", sans-serif; }

  .card {
    position: absolute;
    left: 324px;
    width: 539px;
    height: 333px;
    background: var(--card);
    overflow: hidden;
  }
  .card-front { top: 134px; }
  .card-back { top: 527px; }

  /* Front */
  .brand-mark {
    position: absolute;
    left: 214px; top: 76px;
    width: 112px; height: 112px;
    border-radius: 50%;
    background: var(--logo-circle);
  }
  .brand-name {
    position: absolute;
    left: 0; right: 0; top: 196px;
    text-align: center;
    font-family: "Ubuntu", sans-serif;
    font-weight: 500;
    font-size: 54px;
    line-height: 1;
    color: var(--logo-grey);
  }

  /* Back */
  .name-band {
    position: absolute;
    left: 0; top: 80px;
    width: 539px; height: 80px;
    background: var(--green);
  }
  .referral-fold { position: absolute; left: 411px; top: 60px; }
  .referral-tag {
    position: absolute;
    left: 411px; top: 22px;
    width: 128px; height: 38px;
    background: var(--green);
    color: var(--white);
    font-family: "Ubuntu", sans-serif;
    font-weight: 700;
    font-size: 19px;
    line-height: 38px;
    padding-left: 8px;
  }
  .person-name {
    position: absolute;
    left: 31px; top: 96px;
    font-family: "Ubuntu", sans-serif;
    font-weight: 500;
    font-size: 39px;
    line-height: 1;
    color: var(--white);
    letter-spacing: -0.5px;
  }
  .person-title {
    position: absolute;
    left: 31px; top: 137px;
    font-family: "Mulish", sans-serif;
    font-weight: 800;
    font-size: 6.5px;
    letter-spacing: 0.3px;
    color: var(--white);
  }
  .address {
    position: absolute;
    right: 20px; top: 91px;
    text-align: right;
    font-family: "Ubuntu", sans-serif;
    font-size: 12px;
    line-height: 21px;
    color: var(--white);
  }
  .phones {
    position: absolute;
    left: 180px; top: 196px;
    list-style: none;
  }
  .phones li {
    display: flex;
    align-items: center;
    height: 30px;
    font-family: "Mulish", sans-serif;
    font-weight: 800;
    font-size: 20px;
    letter-spacing: 1.6px;
    color: var(--grey-text);
  }
  .phones svg { width: 20px; height: 18px; margin-right: 11px; fill: var(--green); }
  .website {
    position: absolute;
    left: 0; right: 0; top: 282px;
    text-align: center;
    font-family: "Mulish", sans-serif;
    font-weight: 800;
    font-size: 22px;
    letter-spacing: 3.4px;
    color: var(--green);
  }
</style>
</head>
<body>
  <section class="card card-front">
    <div class="brand-mark"></div>
    <div class="brand-name">Plovenix</div>
  </section>

  <section class="card card-back">
    <div class="name-band"></div>
    <svg class="referral-fold" width="128" height="20" viewBox="0 0 128 20" aria-hidden="true">
      <polygon points="0,0 92,0 128,20 26,20" fill="var(--green-dark)"/>
    </svg>
    <div class="referral-tag">Mpellwood</div>
    <div class="person-name">Marcus Pellwood</div>
    <div class="person-title">DIRECTOR OF SALES AND MARKETING</div>
    <div class="address">Suite 402,<br>18 Brindle Lane,<br>Sydney, NSW 2000</div>
    <ul class="phones">
      <li>
        <svg viewBox="0 0 20 18" aria-label="Office"><path d="M7 2h6a1 1 0 0 1 1 1v2h4a1 1 0 0 1 1 1v10a1 1 0 0 1-1 1H2a1 1 0 0 1-1-1V6a1 1 0 0 1 1-1h4V3a1 1 0 0 1 1-1zm1 1.6V5h4V3.6z"/></svg>
        02 8765 4312
      </li>
      <li>
        <svg viewBox="0 0 20 18" aria-label="Mobile"><path d="M6 0h8a1 1 0 0 1 1 1v16a1 1 0 0 1-1 1H6a1 1 0 0 1-1-1V1a1 1 0 0 1 1-1zm1 3v8h6V3z"/></svg>
        0428 915 603
      </li>
    </ul>
    <div class="website">www.plovenix.com</div>
  </section>
</body>
</html>
```